" O Carro Chefe são Pratos Congelados Sem Glúten, Sem Leite, Sem Soja e Sem Ovo com 70% de Produtos Orgânicos e além disso possuímos linhas com Baixa Carga Glicêmica e Baixo Colesterol "

```html
<!DOCTYPE html>
<html lang="pt-BR">
<head>
<meta charset="utf-8">
<title>Assinatura de e-mail – Verdalia</title>
<link rel="stylesheet" href="https://fonts.googleapis.com/css2?family=Arimo:wght@400;700&display=swap">
<style>
  :root {
    --page-bg: #ecebe8;
    --card-white: #ffffff;
    --card-shade: #e4e4e4;
    --divider: #d9d9d9;
    --green-dark: #2f4a12;
    --text-grey: #4a4a4a;
    --brand-red: #e2452b;
  }
  * { margin: 0; padding: 0; box-sizing: border-box; }
  html, body { width: 1200px; height: 1200px; overflow: hidden; }
  body {
    position: relative;
    background: var(--page-bg);
    font-family: "Arimo", Arial, sans-serif;
  }
  .signature { position: absolute; left: 0; top: 0; width: 1200px; height: 1200px; }
  .signature-shape { position: absolute; left: 0; top: 0; }
  .person-name {
    position: absolute; left: 233px; top: 480px;
    font-size: 30px; font-weight: 700; color: var(--green-dark);
  }
  .person-role {
    position: absolute; left: 400px; top: 510px; width: 102px; text-align: right;
    font-size: 26px; color: var(--green-dark);
  }
  .contact-list, .address {
    position: absolute; left: 160px;
    font-size: 19px; line-height: 21px; color: var(--text-grey);
    list-style: none;
  }
  .contact-list { top: 553px; }
  .contact-list li, .address { display: flex; }
  .contact-list .icon, .address .icon {
    width: 22px; flex: 0 0 22px; display: flex; align-items: center; justify-content: flex-start;
  }
  .contact-list .no-icon { padding-left: 22px; }
  .address { top: 661px; }
  .address .icon { align-items: flex-start; padding-top: 2px; }
  .brand-name {
    position: absolute; left: 700px; top: 560px; width: 418px; text-align: center;
    font-size: 88px; font-weight: 700; color: var(--brand-red); letter-spacing: -1px;
  }
</style>
</head>
<body>
<div class="signature">
  <svg class="signature-shape" width="1200" height="1200" viewBox="0 0 1200 1200" aria-hidden="true">
    <defs>
      <linearGradient id="tabShade" x1="0" y1="0" x2="0" y2="1">
        <stop offset="0" stop-color="#e4e4e4"/>
        <stop offset="1" stop-color="#ffffff"/>
      </linearGradient>
    </defs>
    <polygon points="144,463 722,463 704,510 704,548 144,548" fill="url(#tabShade)"/>
    <rect x="144" y="546" width="562" height="270" fill="#ffffff"/>
    <rect x="700" y="500" width="418" height="316" fill="#ffffff"/>
    <line x1="144" y1="643" x2="690" y2="643" stroke="#d9d9d9" stroke-width="2"/>
  </svg>

  <div class="person-name">Nome Sobrenome</div>
  <div class="person-role">cargo</div>

  <ul class="contact-list">
    <li><span class="icon"><svg width="16" height="16" viewBox="0 0 16 16"><circle cx="8" cy="8" r="7" fill="#2f4a12"/><rect x="4" y="5.5" width="8" height="5.5" fill="#fff"/><path d="M4 5.5 L8 8.5 L12 5.5" stroke="#2f4a12" stroke-width="1" fill="none"/></svg></span>contato@dominio.com</li>
    <li><span class="icon"><svg width="16" height="16" viewBox="0 0 16 16"><circle cx="8" cy="8" r="7" fill="none" stroke="#2f4a12" stroke-width="1.5"/><path d="M5.2 4.5c.6-.4 1.1-.3 1.4.3l.6 1.3c.2.4 0 .8-.3 1l-.4.3c.4 1 1.1 1.7 2.1 2.1l.3-.4c.2-.3.6-.5 1-.3l1.3.6c.6.3.7.8.3 1.4-.6.8-1.500 1-2.4.6C7 10.7 5.3 9 4.6 7 4.2 6 4.4 5.1 5.2 4.5z" fill="#2f4a12"/></svg></span>+55 00 2222-2222</li>
    <li class="no-icon">+55 00 9999-3333&nbsp; / &nbsp;8888-8888</li>
  </ul>

  <div class="address">
    <span class="icon"><svg width="16" height="20" viewBox="0 0 16 20"><path d="M8 1a6 6 0 0 0-6 6c0 4.5 6 12 6 12s6-7.5 6-12a6 6 0 0 0-6-6z" fill="none" stroke="#2f4a12" stroke-width="1.6"/><circle cx="8" cy="7" r="2.2" fill="#2f4a12"/></svg></span>
    <span>Rua Endereço, 1000&nbsp; Complemento<br>Bairro Bairro Bairro<br>CEP: 09000-000&nbsp; Cidade Estado</span>
  </div>

  <div class="brand-name">Verdalia</div>
</div>
</body>
</html>
```